ZOR Clinic

We are a telemedicine based HIV treatment, prevention and hep c clinic looking to help make our online presence known.

Target Market(s)

Future patients. We want to this be informative and have stock images of all different types of people

Industry/Entity Type

Medical

Coding

Coded - Design and coding required

Requirements
Must have
• A Home Page, A page on PrEP, HIV treatment and Hep C. A box in the corner that says book now and a contact us page.

```html
<!DOCTYPE html>
<html lang="en">
<head>
<meta charset="utf-8">
<title>ZOR Clinic — Telemedicine for PrEP, HIV &amp; Hep C</title>
<link href="https://fonts.googleapis.com/css2?family=Inter:wght@400;500;600;700;800&display=swap" rel="stylesheet">
<style>
:root{
  --blue:#0b5cb8;
  --blue-deep:#0a4a9a;
  --green:#6cb33f;
  --green-dark:#4f9a2a;
  --ink:#111418;
  --muted:#555b63;
  --mint:#e9f2ee;
  --paper:#ffffff;
  --line:#dde3e8;
  --footer:#060708;
}
*{box-sizing:border-box;margin:0;padding:0}
html,body{width:1200px;height:4121px;overflow:hidden;background:var(--paper)}
body{font-family:"Inter",Arial,sans-serif;color:var(--ink);position:relative}
.abs{position:absolute}
.accent{color:var(--blue)}
.eyebrow{font-size:12px;font-weight:600;color:var(--blue)}
.btn{display:inline-flex;align-items:center;justify-content:center;gap:6px;border-radius:20px;font-size:10.5px;font-weight:600;height:28px}
.btn-green{background:var(--green);color:#fff}
.btn-ghost{border:1.5px solid #c9ced4;color:var(--ink);background:#fff}
.btn-outline-light{border:1.5px solid rgba(255,255,255,.7);color:#fff}

/* hero */
.hero{left:0;top:0;width:1200px;height:680px;background:#ededee;overflow:hidden}
.hero-photo{position:absolute;left:520px;top:0;width:680px;height:640px;background:linear-gradient(120deg,#f1f1f1 0%,#e4e3e1 35%,#c89a7c 55%,#5fb3a4 75%,#e7e7e7 100%)}
.nav{left:0;top:0;width:1200px;height:60px}
.brand{display:flex;align-items:center;gap:8px;font-weight:700;font-size:15px;color:var(--blue)}
.brand .dot{width:24px;height:24px;border-radius:50%;background:var(--green)}
.nav-links{left:626px;top:23px;display:flex;gap:26px;font-size:10px;font-weight:500}
.nav-links .on{color:var(--green);border-bottom:2px solid var(--green);padding-bottom:8px}
.pill{display:inline-flex;align-items:center;gap:6px;background:#fff;border:1px solid #cfd5da;border-radius:12px;padding:0 10px;height:20px;font-size:9.5px;font-weight:600;color:var(--blue)}
.hero h1{font-size:35px;line-height:39px;font-weight:800;letter-spacing:-.5px}
.hero p{font-size:11px;line-height:16px;color:var(--muted)}
.trust{display:flex;gap:30px}
.trust div{display:flex;align-items:center;gap:10px;font-size:9px;font-weight:600;line-height:11px}
.booknow{left:984px;top:586px;width:180px;height:52px;background:#0c0d0e;border-radius:8px;display:flex;align-items:center;gap:12px;padding:0 12px;color:#fff}
.booknow .ic{width:34px;height:34px;border-radius:6px;background:var(--green);display:flex;align-items:center;justify-content:center}
.booknow b{font-size:12px;display:block}
.booknow span{font-size:8.5px;opacity:.85}

/* services */
.center-head{left:0;width:1200px;text-align:center}
.h2{font-size:28px;font-weight:800;letter-spacing:-.4px}
.sub{font-size:11px;line-height:17px;color:var(--muted)}
.card{background:#fff;border-radius:8px;box-shadow:0 6px 18px rgba(10,30,60,.1);overflow:hidden;width:246px;height:306px}
.card.active{border:1.5px solid #9fbad6}
.card .img{height:166px}
.card h3{font-size:15px;font-weight:700;margin:22px 26px 10px}
.card p{font-size:10px;line-height:16px;color:var(--muted);margin:0 26px}
.card a{display:block;margin:8px 26px 0;font-size:9.5px;font-weight:600;color:var(--blue);text-decoration:none}

/* how it works */
.steps .step{display:flex;gap:16px;position:absolute;left:0}
.step .num{width:46px;height:46px;border-radius:50%;background:var(--green);color:#fff;font-weight:700;font-size:14px;display:flex;align-items:center;justify-content:center;box-shadow:0 0 0 5px rgba(108,179,63,.2)}
.step h4{font-size:15px;font-weight:700;margin-top:2px}
.step p{font-size:10px;line-height:16px;color:var(--muted);margin-top:6px;width:290px}

/* stats */
.stats{left:0;top:1754px;width:1200px;height:196px;background:linear-gradient(90deg,#0a4c9e,#0b63c4 50%,#0a4c9e)}
.stat{position:absolute;top:72px;width:200px;text-align:center;color:#fff}
.stat b{display:block;font-size:29px;font-weight:800}
.stat span{display:block;font-size:10px;line-height:16px;margin-top:6px;opacity:.9}
.divider{position:absolute;top:70px;width:1px;height:74px;background:rgba(255,255,255,.35)}

/* community */
.checks li{list-style:none;display:flex;align-items:center;gap:8px;font-size:10.5px;margin-bottom:7px}
.checks li i{width:10px;height:10px;border-radius:50%;background:var(--green);display:inline-block}
.ph{position:absolute;border-radius:8px}

/* stories */
.review{position:absolute;top:2616px;height:174px;background:#fff;border-radius:8px;box-shadow:0 6px 20px rgba(10,30,60,.1);padding:28px 30px}
.stars{color:#f4a51c;font-size:12px;letter-spacing:1px}
.review q{display:block;font-size:10.5px;line-height:16.5px;color:#333;margin-top:12px;quotes:none}
.who{display:flex;align-items:center;gap:10px;margin-top:14px}
.who i{width:26px;height:26px;border-radius:50%;background:#5a4a3e}
.who b{font-size:9.5px;display:block}
.who span{font-size:7.5px;color:#888}

/* faq */
.faq{left:306px;top:3038px;width:590px;border:1px solid var(--line);border-radius:8px;background:#fff}
.faq .item{border-bottom:1px solid var(--line);padding:0 32px;display:flex;justify-content:space-between;align-items:center;height:52px;font-size:14px;font-weight:700}
.faq .item:last-child{border-bottom:none}
.faq .open{height:114px;display:block;padding-top:22px}
.faq .open p{font-size:10px;line-height:16px;color:var(--muted);font-weight:400;margin-top:10px;width:500px}
.chev{width:20px;height:20px;border-radius:50%;background:#eef1f3;display:flex;align-items:center;justify-content:center}

/* footer */
.footer{left:0;top:3800px;width:1200px;height:321px;background:var(--footer);color:#fff}
.fcol h5{font-size:16px;font-weight:700;margin-bottom:10px}
.fcol li{list-style:none;font-size:9.5px;line-height:19px;color:#d3d6da;display:flex;align-items:center;gap:8px}
.fcol li i{width:7px;height:7px;border-radius:50%;background:var(--blue);display:inline-block}
</style>
</head>
<body>

<!-- hero -->
<section class="abs hero">
  <div class="hero-photo" role="img" aria-label="Woman with headset on a video consultation with a doctor on her laptop"></div>
  <svg class="abs" style="left:0;top:560px" width="1200" height="120" viewBox="0 0 1200 120">
    <path d="M0 70 C260 10 600 40 1200 20 L1200 120 L0 120Z" fill="#0b5cb8"/>
    <path d="M0 110 C300 40 640 62 1200 70 L1200 120 L0 120Z" fill="#ffffff"/>
  </svg>
</section>

<nav class="abs nav">
  <div class="abs brand" style="left:150px;top:16px"><i class="dot"></i>ZOR Clinic</div>
  <div class="abs nav-links"><span class="on">Home</span><span>PrEP</span><span>HIV Treatment</span><span>Hep C</span><span>Contact Us</span></div>
  <div class="abs btn btn-green" style="left:944px;top:16px;width:106px;height:29px">▦ Book Now ›</div>
</nav>

<div class="abs pill" style="left:150px;top:186px">✓ Telemedicine · HIV · PrEP · Hep C</div>
<div class="abs hero" style="background:none;width:auto;height:auto;top:216px;left:150px;overflow:visible">
  <h1>Modern Care for PrEP,<br><span class="accent">HIV &amp; Hep C From Home</span>.</h1>
  <p style="margin-top:14px;width:350px">Empowering healthcare tailored for everyone. Access discreet consultations, fast lab work orders, and direct prescription delivery without ever stepping foot in a waiting room.</p>
</div>
<div class="abs btn btn-green" style="left:150px;top:361px;width:163px">▦ Book a confidential visit ›</div>
<div class="abs btn btn-ghost" style="left:322px;top:361px;width:138px">Is PrEP right for me?</div>
<div class="abs trust" style="left:150px;top:420px">
  <div><svg width="22" height="26" viewBox="0 0 22 26"><path d="M11 2 L20 6 V13 C20 19 11 24 11 24 C11 24 2 19 2 13 V6Z" fill="none" stroke="#0b5cb8" stroke-width="1.6"/><path d="M7 13l3 3 5-6" fill="none" stroke="#0b5cb8" stroke-width="1.6"/></svg>HIPAA<br>Private</div>
  <div><svg width="26" height="22" viewBox="0 0 26 22"><rect x="2" y="2" width="22" height="15" rx="2" fill="none" stroke="#0b5cb8" stroke-width="1.6"/><path d="M8 20h10" stroke="#0b5cb8" stroke-width="1.6"/></svg>100% Online<br>Care</div>
  <div><svg width="24" height="22" viewBox="0 0 24 22"><path d="M12 20 C4 14 2 10 2 7 A5 5 0 0 1 12 5 A5 5 0 0 1 22 7 C22 10 20 14 12 20Z" fill="none" stroke="#0b5cb8" stroke-width="1.6"/></svg>Judgment-Free<br>Support</div>
</div>

<a class="abs booknow"><span class="ic"><svg width="18" height="18" viewBox="0 0 18 18"><rect x="2" y="3" width="14" height="13" rx="2" fill="none" stroke="#fff" stroke-width="1.5"/><path d="M2 7h14M6 1v4M12 1v4" stroke="#fff" stroke-width="1.5"/></svg></span><span><b>Book Now</b><span>Same-week video visits</span></span></a>

<!-- services -->
<div class="abs center-head" style="top:710px">
  <div class="eyebrow">Our services</div>
  <div class="h2" style="margin-top:6px">Prevention, treatment, and cure — <span class="accent">online</span></div>
  <div class="sub" style="margin-top:8px">Evidence-based care designed around your life. Lab orders, prescriptions, and follow-up<br>coordinated through secure telehealth.</div>
</div>
<svg class="abs" style="left:950px;top:778px" width="50" height="30"><rect x="38" y="2" width="9" height="9" fill="#6cb33f"/><rect x="26" y="12" width="8" height="8" fill="#0b5cb8"/><rect x="14" y="20" width="6" height="6" fill="#6cb33f"/></svg>
<svg class="abs" style="left:200px;top:1096px" width="52" height="48"><path d="M16 0h10v16h16v10H26v20H16V26H0V16h16Z" fill="#6cb33f"/></svg>
<div class="abs card" style="left:224px;top:816px">
  <div class="img" role="img" aria-label="Group of adults stretching together outdoors" style="background:linear-gradient(160deg,#6d8a4b,#a7a083 60%,#c9b9a3)"></div>
  <h3>PrEP</h3><p>Daily or on-demand PrEP options to help prevent HIV. Ongoing monitoring, refills, and supportive counseling — all virtual.</p><a>Learn More ›</a>
</div>
<div class="abs card active" style="left:477px;top:816px">
  <div class="img" role="img" aria-label="Clinician talking with a patient on a sofa" style="background:linear-gradient(160deg,#cfd4d8,#9aa7b2 60%,#e6e8ea)"></div>
  <h3>HIV Treatment</h3><p>Modern antiretroviral therapy, lab monitoring, and stigma-free support so you can thrive with an undetectable viral load.</p><a>Learn More ›</a>
</div>
<div class="abs card" style="left:730px;top:816px">
  <div class="img" role="img" aria-label="Smiling woman with curly hair" style="background:linear-gradient(160deg,#b9b6b1,#7a5840 55%,#cfcac4)"></div>
  <h3>Hepatitis C</h3><p>Short-course oral treatments that cure Hep C for most people. Screening, staging, and cure confirmation from home.</p><a>Learn More ›</a>
</div>

<!-- how it works -->
<svg class="abs" style="left:0;top:1190px" width="1200" height="564" viewBox="0 0 1200 564" preserveAspectRatio="none"><path d="M0 110 C320 20 700 70 1200 0 V564 H0Z" fill="#e9f2ee"/></svg>
<div class="abs" role="img" aria-label="Person on a video call with a smiling doctor on a laptop" style="left:181px;top:1322px;width:419px;height:345px;border-radius:10px;background:linear-gradient(135deg,#6b5547,#d9d4cb 45%,#7aa3a9 80%,#3c5e7a)"></div>
<div class="abs" style="left:662px;top:1338px">
  <div class="eyebrow">How it works</div>
  <div class="h2" style="margin-top:6px;line-height:34px">From “<span class="accent">hello</span>” to treated in<br>three simple steps.</div>
</div>
<svg class="abs" style="left:684px;top:1480px" width="2" height="150"><line x1="1" y1="0" x2="1" y2="150" stroke="#b9d7a8" stroke-dasharray="4 4"/></svg>
<div class="abs steps" style="left:662px;top:1454px">
  <div class="step" style="top:0"><div class="num">01</div><div><h4>Book a private visit</h4><p>Pick a time that works — evenings and weekends included. Tell us as much or as little as you like.</p></div></div>
  <div class="step" style="top:74px"><div class="num">02</div><div><h4>Meet your clinician on video</h4><p>A licensed provider reviews your history, answers questions, and orders labs at a location near you (or a home kit).</p></div></div>
  <div class="step" style="top:150px"><div class="num">03</div><div><h4>Meds arrive at your door</h4><p>Prescriptions ship in plain, discreet packaging — or we send them to your local pharmacy. Follow-ups stay virtual.</p></div></div>
</div>

<!-- stats -->
<section class="abs stats">
  <div class="stat" style="left:175px"><b>99%</b><span>PrEP reduction in HIV risk from<br>sex, taken as prescribed</span></div>
  <div class="divider" style="left:380px"></div>
  <div class="stat" style="left:386px"><b>&gt;95%</b><span>Hep C cure rate with modern<br>antiviral treatment</span></div>
  <div class="divider" style="left:593px"></div>
  <div class="stat" style="left:607px"><b>U = U</b><span>Undetectable viral load means<br>zero sexual transmission</span></div>
  <div class="divider" style="left:825px"></div>
  <div class="stat" style="left:825px"><b>50</b><span>States where our clinicians<br>can see you virtually</span></div>
</section>

<!-- community -->
<div class="abs" style="left:182px;top:2078px">
  <div class="eyebrow">For everyone</div>
  <div class="h2" style="margin-top:4px;line-height:34px">Care that looks like<br>your <span class="accent">community</span>.</div>
  <p class="sub" style="margin-top:14px;width:360px;font-size:10px;line-height:16px">HIV and Hep C don't discriminate — and neither do we. Our clinicians are trained in LGBTQ+ affirming, culturally competent, harm-reduction care for people of every identity, age, and background.</p>
  <ul class="checks" style="margin-top:12px">
    <li><i></i>LGBTQ+ affirming &amp; sex-positive</li>
    <li><i></i>Trans &amp; nonbinary competent</li>
    <li><i></i>Harm-reduction, never shame-based</li>
    <li><i></i>Bilingual care coordinators</li>
  </ul>
</div>
<div class="ph" role="img" aria-label="Portrait of a smiling woman" style="left:632px;top:2037px;width:134px;height:216px;background:linear-gradient(#f2a43c,#d98a2a)"></div>
<div class="ph" role="img" aria-label="Portrait of a young person in a black t-shirt" style="left:632px;top:2259px;width:134px;height:215px;background:linear-gradient(#dcdad6,#3a3a3c)"></div>
<div class="ph" role="img" aria-label="Portrait of a laughing young man" style="left:773px;top:2037px;width:136px;height:155px;background:linear-gradient(135deg,#e0a070,#6a4a3a 60%,#c46a6a)"></div>
<div class="ph" role="img" aria-label="Two friends laughing together" style="left:773px;top:2198px;width:136px;height:109px;background:linear-gradient(135deg,#c9c0b4,#6d5546)"></div>
<div class="ph" role="img" aria-label="Group of friends standing together" style="left:773px;top:2314px;width:136px;height:160px;background:linear-gradient(#d8d5d0,#b9ad9a)"></div>
<div class="ph" role="img" aria-label="Older man at home" style="left:914px;top:2037px;width:136px;height:155px;background:linear-gradient(135deg,#cfd3d6,#4e6e9e)"></div>
<div class="ph" role="img" aria-label="Young man in a blue sweater" style="left:914px;top:2198px;width:136px;height:216px;background:linear-gradient(#e3e3e3,#3f66b8 70%,#e3e3e3)"></div>

<!-- stories -->
<div class="abs" style="left:0;top:2416px;width:1200px;height:454px;background:linear-gradient(#eef0f1,#e6e9ea)"></div>
<div class="abs center-head" style="top:2540px">
  <div class="eyebrow">Patient stories</div>
  <div class="h2" style="margin-top:4px">Real <span class="accent">people</span>. Real peace of mind.</div>
</div>
<svg class="abs" style="left:918px;top:2552px" width="120" height="70"><rect x="90" y="2" width="24" height="24" fill="#6cb33f"/><rect x="40" y="34" width="24" height="24" fill="#6cb33f"/><rect x="2" y="50" width="14" height="14" fill="#6cb33f"/><rect x="92" y="54" width="12" height="12" fill="#0b5cb8"/></svg>
<div class="review" style="left:187px;width:391px">
  <div class="stars">★★★★★</div>
  <q>“Starting PrEP felt scary until I realized I could do the whole thing from my bedroom. No waiting room, no stares. My meds showed up in a box that looked like it could've been socks.”</q>
  <div class="who"><i></i><div><b>Marco, 24</b><span>PrEP patient · Texas</span></div></div>
</div>
<div class="review" style="left:586px;width:427px">
  <div class="stars">★★★★★</div>
  <q>“I'd been putting off Hep C treatment for years. Twelve weeks of pills later, I'm cured. My provider checked in on video every step — it genuinely changed my life.”</q>
  <div class="who"><i style="background:#222"></i><div><b>Dana, 41</b><span>Hep C cured · Ohio</span></div></div>
</div>

<!-- faq -->
<div class="abs center-head" style="top:2958px">
  <div class="eyebrow">Good to know</div>
  <div class="h2" style="margin-top:4px">Questions <span class="accent">people</span> actually ask us</div>
</div>
<div class="abs faq">
  <div class="item open"><div style="display:flex;justify-content:space-between"><span>Is telemedicine really enough for HIV or Hep C care?</span><span class="chev">⌄</span></div><p>Yes. Modern HIV and Hep C care is largely lab-driven, and those labs can be drawn at a location near you (or via home kits). Your clinician reviews results on video and adjusts treatment — the same standard of care as in-person clinics, validated by major health systems nationwide.</p></div>
  <div class="item">Will my visit be private?<span class="chev">⌃</span></div>
  <div class="item">Do you take insurance?<span class="chev">⌃</span></div>
  <div class="item">How fast can I be seen?<span class="chev">⌃</span></div>
  <div class="item">Do I need to be tech-savvy?<span class="chev">⌃</span></div>
</div>

<!-- cta -->
<svg class="abs" style="left:0;top:3430px" width="1200" height="420" viewBox="0 0 1200 420" preserveAspectRatio="none">
  <path d="M0 100 C400 120 800 20 1200 10 V420 H0Z" fill="#0b5cb8"/>
  <path d="M0 360 C360 330 800 300 1200 250 V420 H0Z" fill="#060708"/>
</svg>
<div class="abs center-head" style="top:3545px;color:#fff">
  <div class="h2">Your health, on your terms.</div>
  <div class="sub" style="color:#dbe6f5;margin-top:10px">Book a confidential video visit today — most patients are seen within the week,<br>with meds delivered to their door shortly after.</div>
</div>
<div class="abs btn btn-green" style="left:482px;top:3638px;width:106px">▦ Book Now ›</div>
<div class="abs btn btn-outline-light" style="left:595px;top:3638px;width:126px">Contact our Team</div>

<!-- footer -->
<footer class="abs footer">
  <div class="abs brand" style="left:150px;top:86px;color:#fff"><i class="dot"></i>ZOR Clinic</div>
  <p class="abs" style="left:150px;top:130px;width:240px;font-size:9.5px;line-height:16px;color:#d3d6da">Confidential, judgment-free telemedicine for HIV prevention and treatment and Hepatitis C care — delivered by clinicians who treat you like a neighbor, not a chart.</p>
  <div class="abs" style="left:150px;top:199px;font-size:9.5px;color:#d3d6da;display:flex;align-items:center;gap:8px"><i style="width:9px;height:9px;border-radius:50%;background:var(--green);display:inline-block"></i>HIPAA-compliant · Encrypted video visits</div>
  <div class="abs fcol" style="left:462px;top:90px"><h5>Services</h5><ul><li>PrEP for HIV prevention</li><li>HIV treatment &amp; care</li><li>Hepatitis C cure</li><li>Lab work &amp; referrals</li></ul></div>
  <div class="abs fcol" style="left:662px;top:90px"><h5>Clinic</h5><ul><li>How it works</li><li>Contact us</li><li>Insurance &amp; pricing</li><li>Patient portal</li></ul></div>
  <div class="abs fcol" style="left:819px;top:90px"><h5>Reach us</h5><ul><li><i></i>(800) 555-0199</li><li><i></i>care@zorclinic.example</li><li><i></i>100% virtual — caring for patients in all 50 states</li><li><i></i>Mon–Fri 8a–8p · Sat 9a–2p (ET)</li></ul></div>
  <div class="abs" style="left:1103px;top:260px;width:30px;height:30px;border-radius:50%;background:var(--green-dark);color:#fff;display:flex;align-items:center;justify-content:center;font-size:12px">⌃</div>
  <div class="abs" style="left:0;top:294px;width:1200px;text-align:center;font-size:9px;color:#c4c8cc">© 2026 ZOR Clinic. All rights reserved.</div>
</footer>

</body>
</html>
```